Folder Rotterdam Walking Tours and Bike Tours

We need a folder to inform potential guests which tours we provide in Rotterdam. We have regular Walking Tours and Bike Tours. We would like to see designs that emphasize something fun to do. Please make it a fresh and vivid design. If it is possible, use the colors green and white. These are the colors of Rotterdam and of our company.

PLEASE FIRST READ THE UPLOADED WORD DOCUMENT FOR A FULL DETAILED DESCRIPTION.

Target Market(s)

Tourists (couples, solo travelers, small groups) in Rotterdam

Industry/Entity Type

Tourism

Font styles to use
Serif

Colors

Designer to choose colors to be used in the design.

Requirements
Must have
• - Follow the description. See attachment Word document.
• - Use pictures that I have uploaded. See attachments.
• - it's NOT necessary to use every uploaded picture.
• - Make a fresh/colorful/vivid design
• - Create an inviting and happy atmosphere.
• - It must be a 3 PAGE FOLDED BROCHURE.
• - Emphasize our Quelloscope rating: Quelloscope #1 Outdoor Activity Rotterdam
Nice to have
• - Where possible, use the colors green and white (colors of company and of the city of Rotterdam).

```html
<!DOCTYPE html>
<html lang="en">
<head>
<meta charset="utf-8">
<title>Roamwise Rotterdam – Tri-fold Brochure</title>
<link rel="stylesheet" href="https://fonts.googleapis.com/css2?family=Source+Sans+3:wght@400;600;700&family=Courgette&display=swap">
<style>
  :root{
    --green:#479a5d;
    --green-dark:#3b8a50;
    --green-light:#8fc79d;
    --white:#ffffff;
    --ink:#2b2b2b;
    --charcoal:#262626;
    --charcoal-2:#3a3a3a;
    --backdrop:#d3d5d8;
  }
  *{box-sizing:border-box;margin:0;padding:0}
  html,body{width:848px;height:1200px;overflow:hidden}
  body{background:var(--backdrop);font-family:"Source Sans 3",Arial,sans-serif;color:var(--ink);position:relative}

  .sheet{position:absolute;left:47px;width:753px;display:flex;background:var(--white);box-shadow:3px 4px 8px rgba(0,0,0,.28)}
  .sheet--outside{top:42px;height:532px}
  .sheet--inside{top:624px;height:531px}
  .panel{position:relative;width:251px;height:100%;overflow:hidden}
  .panel + .panel{border-left:1px solid rgba(0,0,0,.08)}
  .abs{position:absolute}

  .photo{position:absolute;left:0;width:100%}
  .footer-bar{position:absolute;left:0;bottom:0;width:100%;height:22px;background:var(--green);color:var(--white);
    font-size:11px;letter-spacing:.6px;display:flex;align-items:center;justify-content:center}

  /* Panel: private tours */
  .photo--group{top:0;height:233px;background:
    radial-gradient(ellipse 40% 30% at 30% 55%,rgba(214,72,72,.75),transparent 70%),
    radial-gradient(ellipse 35% 30% at 62% 60%,rgba(58,168,140,.7),transparent 70%),
    radial-gradient(ellipse 45% 25% at 70% 25%,rgba(238,226,196,.9),transparent 70%),
    linear-gradient(180deg,#d8d2bf 0%,#a8886a 35%,#7a5d48 70%,#4f4540 100%)}
  .tab{position:absolute;left:0;top:223px;width:199px;height:22px;background:var(--green);border-radius:0 11px 11px 0;
    color:var(--white);font-size:11.5px;line-height:22px;padding-left:14px}
  .copy{position:absolute;left:14px;width:225px;font-size:9px;line-height:12.5px;text-align:justify}
  .copy p + p{margin-top:12px}
  .photo--skyline{top:372px;height:138px;background:
    radial-gradient(ellipse 30% 40% at 20% 55%,rgba(92,112,130,.55),transparent 70%),
    radial-gradient(ellipse 40% 25% at 70% 90%,rgba(196,150,96,.55),transparent 70%),
    linear-gradient(180deg,#f7f9fb 0%,#dfe6ec 35%,#9fb0c0 65%,#6d7c8a 100%)}

  /* Panel: cover centre */
  .panel--dark{background:linear-gradient(180deg,var(--charcoal-2),var(--charcoal))}
  .photo--circle{position:absolute;left:57px;top:30px;width:134px;height:134px;border-radius:50%;border:3px solid var(--white);
    background:
    radial-gradient(circle at 30% 65%,rgba(220,170,120,.85),transparent 40%),
    radial-gradient(circle at 72% 60%,rgba(70,120,170,.8),transparent 40%),
    radial-gradient(circle at 50% 15%,rgba(120,180,220,.95),transparent 45%),
    linear-gradient(180deg,#cfe2f0,#8a6e58 70%,#4d433b)}
  .brand{position:absolute;left:0;width:100%;text-align:center;color:var(--white)}
  .brand__name{font-weight:600;font-size:40px;line-height:1}
  .brand__city{font-size:7.5px;letter-spacing:6px;margin-top:3px;padding-left:40px}
  .tagline{position:absolute;left:0;width:100%;top:250px;text-align:center;font-family:"Courgette",cursive;color:var(--green-light);font-size:16.5px;line-height:22px}
  .rating-mark{position:absolute;left:112px;top:313px;width:26px;height:26px;border-radius:50%;border:2px solid var(--white)}
  .rating-text{position:absolute;left:0;width:100%;top:350px;text-align:center;color:var(--white);font-size:11px;line-height:16px;text-transform:uppercase}
  .social{position:absolute;top:395px;left:0;width:100%;display:flex;justify-content:center;gap:11px}
  .social span{width:22px;height:22px;border-radius:50%;border:1.5px solid var(--green);background:rgba(71,154,93,.25)}
  .contact{position:absolute;left:0;width:100%;top:433px;text-align:center;color:var(--white);font-size:11px;line-height:19px}

  /* Panel: front cover */
  .photo--bikers{top:150px;height:250px;background:
    radial-gradient(ellipse 18% 22% at 20% 60%,rgba(60,120,200,.85),transparent 70%),
    radial-gradient(ellipse 18% 22% at 42% 62%,rgba(230,140,140,.8),transparent 70%),
    radial-gradient(ellipse 18% 22% at 64% 60%,rgba(214,120,50,.85),transparent 70%),
    radial-gradient(ellipse 18% 22% at 85% 62%,rgba(40,60,120,.85),transparent 70%),
    linear-gradient(180deg,#5f9fdc 0%,#a9cbe8 35%,#c9d6de 48%,#7f7a74 75%,#4a4a48 100%)}
  .cover-brand{position:absolute;right:22px;top:28px;text-align:right;color:var(--white)}
  .cover-brand .brand__name{font-size:38px}
  .cover-brand .brand__city{padding-left:0;letter-spacing:6px}
  .rating-row{position:absolute;left:32px;top:133px;display:flex;align-items:center;gap:9px;font-size:9px;font-weight:600;line-height:12px;text-transform:uppercase;color:var(--ink)}
  .rating-row i{display:block;width:22px;height:22px;border-radius:50%;background:var(--ink)}
  .modes{position:absolute;top:408px;left:0;width:100%;display:flex;justify-content:center;gap:9px}
  .mode{width:45px;height:45px;border-radius:50%;background:var(--green);border:2px solid var(--white);box-shadow:0 0 0 1.5px var(--green);
    color:var(--white);font-size:4.5px;font-weight:700;text-transform:uppercase;display:flex;align-items:flex-end;justify-content:center;padding-bottom:7px}
  .cover-line{position:absolute;left:0;width:100%;top:462px;text-align:center;font-size:15.5px;line-height:20px;text-transform:uppercase;color:var(--ink)}

  /* Inside tour panels */
  .tour .photo{top:0;height:240px}
  .photo--bridge{background:
    radial-gradient(ellipse 50% 14% at 45% 70%,rgba(200,60,60,.55),transparent 70%),
    radial-gradient(ellipse 25% 25% at 10% 8%,rgba(60,90,40,.85),transparent 70%),
    linear-gradient(180deg,#6fa6dc 0%,#b3d0ea 35%,#dfe7ee 52%,#9a948c 75%,#6d6a66 100%)}
  .photo--park{background:
    radial-gradient(ellipse 25% 18% at 62% 45%,rgba(170,70,50,.8),transparent 70%),
    radial-gradient(ellipse 30% 45% at 15% 40%,rgba(90,140,50,.9),transparent 70%),
    radial-gradient(ellipse 30% 40% at 85% 35%,rgba(110,160,60,.85),transparent 70%),
    linear-gradient(180deg,#6fa0d8 0%,#a9c9e6 25%,#5f8f3e 50%,#3e6a2e 72%,#4f5f56 100%)}
  .photo--square{background:
    radial-gradient(ellipse 15% 25% at 12% 60%,rgba(230,180,40,.75),transparent 70%),
    radial-gradient(ellipse 20% 25% at 90% 55%,rgba(200,50,50,.7),transparent 70%),
    radial-gradient(ellipse 25% 25% at 90% 15%,rgba(90,150,60,.8),transparent 70%),
    linear-gradient(180deg,#bcd3e6 0%,#d8dde0 30%,#8c8f91 55%,#55575a 80%,#3f4144 100%)}
  .tour__wave{position:absolute;left:0;top:170px;width:251px;height:80px}
  .tour__body{position:absolute;left:0;top:240px;width:100%;bottom:31px;background:linear-gradient(180deg,#fff 0%,#fff 55%,#e8eef2 100%)}
  .tour__title{position:absolute;left:14px;top:2px;font-size:15.5px;font-weight:400;letter-spacing:-.1px;color:var(--green-dark);white-space:nowrap}
  .tour__text{position:absolute;left:14px;top:28px;width:224px;font-size:9.2px;line-height:12.5px;text-align:justify}
  .tour__label{position:absolute;left:14px;top:96px;font-size:10px;font-weight:700}
  .tour__times{position:absolute;left:14px;top:113px;font-size:8.8px;line-height:12.5px}
  .tour__times b{font-weight:400;color:var(--green-dark)}
  .price{position:absolute;left:16px;top:158px;width:219px;height:39px;border:1px solid var(--green);border-radius:5px;
    font-size:8.6px;font-weight:600;text-align:center;line-height:13px;padding-top:6px;background:rgba(255,255,255,.85)}
  .facts{position:absolute;left:14px;top:205px;font-size:6.6px;line-height:10.5px}
  .meet{position:absolute;left:14px;top:229px;width:224px;font-size:8.6px;line-height:11px}
  .tour__footer{position:absolute;left:0;bottom:0;width:100%;height:31px;background:var(--green);color:var(--white);
    display:flex;align-items:center;justify-content:center;gap:7px;font-size:12px;letter-spacing:.5px}
  .tour__footer svg{width:13px;height:13px}
</style>
</head>
<body>

<section class="sheet sheet--outside">

  <div class="panel panel--private">
    <div class="photo photo--group" role="img" aria-label="Photo of a cheerful tour group posing in front of a café"></div>
    <svg class="abs" style="left:0;top:0" width="251" height="60" viewBox="0 0 251 60" aria-hidden="true">
      <path d="M0 0H251V14C180 20 90 38 0 60Z" fill="var(--green)"/>
    </svg>
    <div class="tab">Private tours</div>
    <div class="copy" style="top:262px">
      <p>You name it, we definitely got it! We offer walking tours, bike tours, Tuk Tuk Tours and Kick Scooter Tours. Customize as you please.</p>
      <p>Discuss your wishes with us and we will make sure that every tailor-made tour will be a success.</p>
      <p>You can look forward to an entertaining tour which will be one of the highlights of your stay in Rotterdam.</p>
    </div>
    <div class="photo photo--skyline" role="img" aria-label="Photo of the Rotterdam skyline with a waving flag"></div>
    <div class="footer-bar">www.roamwiserotterdam.com</div>
  </div>

  <div class="panel panel--dark">
    <svg class="abs" style="left:0;top:0" width="251" height="45" viewBox="0 0 251 45" aria-hidden="true">
      <path d="M0 0H251V12C170 8 90 20 0 44Z" fill="var(--green)"/>
    </svg>
    <div class="photo--circle" role="img" aria-label="Round photo of a smiling group at a terrace"></div>
    <div class="brand" style="top:178px">
      <div class="brand__name">Roamwise</div>
      <div class="brand__city">ROTTERDAM</div>
    </div>
    <div class="tagline">Experience the city with<br>a local tour guide</div>
    <span class="rating-mark" aria-hidden="true"></span>
    <div class="rating-text">Quelloscope #1<br>Outdoor Activity Rotterdam</div>
    <div class="social" aria-hidden="true"><span></span><span></span><span></span><span></span></div>
    <div class="contact">
      Tel. +31 (0)10 55 01 234<br>
      WhatsApp: +31 (0)6 12 34 56 78<br>
      hello@roamwiserotterdam.com
    </div>
    <div class="footer-bar">www.roamwiserotterdam.com</div>
  </div>

  <div class="panel panel--cover">
    <div class="photo photo--bikers" role="img" aria-label="Photo of four smiling guides with bikes by the river, with Dutch and British flags"></div>
    <svg class="abs" style="left:0;top:0" width="251" height="160" viewBox="0 0 251 160" aria-hidden="true">
      <path d="M0 0H251V82C170 86 80 100 0 118Z" fill="var(--green)"/>
      <path d="M0 118C80 100 170 86 251 82V92C170 96 90 108 0 128Z" fill="#bfc3c6"/>
      <path d="M0 128C90 108 170 96 251 92V160H0Z" fill="var(--white)"/>
    </svg>
    <svg class="abs" style="left:0;top:370px" width="251" height="40" viewBox="0 0 251 40" aria-hidden="true">
      <path d="M0 20C90 0 170 4 251 16V40H0Z" fill="var(--green)"/>
      <path d="M0 26C90 6 170 10 251 22V40H0Z" fill="var(--white)"/>
    </svg>
    <div class="cover-brand">
      <div class="brand__name">Roamwise</div>
      <div class="brand__city">ROTTERDAM</div>
    </div>
    <div class="rating-row"><i aria-hidden="true"></i><span>Quelloscope #1<br>Outdoor Activity Rotterdam</span></div>
    <div class="modes">
      <div class="mode">Walking</div>
      <div class="mode">Cycling</div>
      <div class="mode">Kick Scooter</div>
      <div class="mode">Tuk Tuk</div>
    </div>
    <div class="cover-line">Experience the city with<br>a local tour guide</div>
    <div class="footer-bar">www.roamwiserotterdam.com</div>
  </div>
</section>

<section class="sheet sheet--inside">

  <div class="panel tour">
    <div class="photo photo--bridge" role="img" aria-label="Photo of a bike tour group in front of the Erasmus Bridge"></div>
    <svg class="tour__wave" viewBox="0 0 251 80" aria-hidden="true">
      <path d="M0 62C80 42 170 36 251 44V48C170 40 80 46 0 66Z" fill="var(--green)"/>
      <path d="M0 66C80 46 170 40 251 48V80H0Z" fill="var(--white)"/>
    </svg>
    <div class="tour__body">
      <h2 class="tour__title">Rotterdam Highlights Bike Tour</h2>
      <p class="tour__text">Discover EVERY highlight of Rotterdam with this bike tour! Visit top attractions like the Erasmus Bridge, Market Hall, Euromast and all the other main sights during this epic 3-hour bike tour.</p>
      <div class="tour__label">AVAILABILITY:</div>
      <div class="tour__times">
        <b>Friday:</b> 10.30 Dutch Tour / 11.00 English Tour<br>
        <b>Saturday:</b> 10.30 Dutch Tour / 11.00 English Tour<br>
        <b>Sunday:</b> 14.00 English Tour / 14.30 Dutch Tour
      </div>
      <div class="price">Price per person: €15 (bring your own bike)<br>€26 with 3-speed rental bike</div>
      <div class="facts">• Max. 15 participants<br>• Duration: 3 hours</div>
      <div class="meet">Meeting point: Spoke Harbour Bikes. Address: Kadeweg 12, 3011 AB Rotterdam.</div>
    </div>
    <div class="tour__footer">
      <svg viewBox="0 0 16 16" aria-hidden="true"><circle cx="8" cy="8" r="6.5" fill="none" stroke="#fff" stroke-width="1.4"/><path d="M5.6 4.8l1.3-.3.7 1.7-.8.6c.4.9 1 1.5 1.9 1.9l.6-.8 1.7.7-.3 1.3C8.5 10 6 7.5 5.6 4.8Z" fill="#fff"/></svg>
      +31 (0)6 12 34 56 78
    </div>
  </div>

  <div class="panel tour">
    <div class="photo photo--park" role="img" aria-label="Photo of a park pond with a fountain and a historic villa"></div>
    <svg class="tour__wave" viewBox="0 0 251 80" aria-hidden="true">
      <path d="M0 44C80 40 170 46 251 62V66C170 50 80 44 0 48Z" fill="var(--green)"/>
      <path d="M0 48C80 44 170 50 251 66V80H0Z" fill="var(--white)"/>
    </svg>
    <div class="tour__body">
      <h2 class="tour__title">Rotterdam Hidden Gems Bike Tour</h2>
      <p class="tour__text">Get ready to swerve off the beaten path with this unique bike tour! Discover a timber church, cycle through an underground tunnel and get outside the city center to experience Rotterdam's beautiful and tranquil places. Enjoy Rotterdam like a local!</p>
      <div class="tour__label">AVAILABILITY:</div>
      <div class="tour__times">
        <b>Friday:</b> 14.00 Dutch Tour / 14.30 English Tour<br>
        <b>Saturday:</b> 14.00 Dutch Tour / 14.30 English Tour<br>
        <b>Sunday:</b> 10.30 English Tour / 11.00 Dutch Tour
      </div>
      <div class="price">Price per person: : €15 (bring your own bike)<br>€26 with 3-speed rental bike</div>
      <div class="facts">• Max. 15 participants<br>• Duration: 3 hours</div>
      <div class="meet">Meeting point: Spoke Harbour Bikes. Address: Kadeweg 12, 3011 AB Rotterdam.</div>
    </div>
    <div class="tour__footer">
      <svg viewBox="0 0 16 16" aria-hidden="true"><circle cx="8" cy="8" r="6.5" fill="none" stroke="#fff" stroke-width="1.4"/><rect x="4.5" y="5.5" width="7" height="5" fill="none" stroke="#fff" stroke-width="1"/><path d="M4.5 5.5L8 8.3 11.5 5.5" fill="none" stroke="#fff" stroke-width="1"/></svg>
      hello@roamwiserotterdam.com
    </div>
  </div>

  <div class="panel tour">
    <div class="photo photo--square" role="img" aria-label="Photo of a walking tour group listening to a guide in a city square"></div>
    <svg class="tour__wave" viewBox="0 0 251 80" aria-hidden="true">
      <path d="M0 64C80 52 170 48 251 40V44C170 52 80 56 0 68Z" fill="var(--green)"/>
      <path d="M0 68C80 56 170 52 251 44V80H0Z" fill="var(--white)"/>
    </svg>
    <div class="tour__body">
      <h2 class="tour__title">Rotterdam Free Walking Tour</h2>
      <p class="tour__text">This is the perfect tour to start your city trip. This walking tour will give you an overview of the top attractions in Rotterdam. Markthal and Witte de Withstraat, here we come!</p>
      <div class="tour__label">AVAILABILITY:</div>
      <div class="tour__times">
        <b>Monday to Thurday:</b> 11.00 English Tours<br>
        <b>Saturday:</b> 11.00 Dutch Tour / 14.00 English Tour<br>
        Sunday:
      </div>
      <div class="price">Price per person: €15 (bring your own bike)<br>€26 with 3-speed rental bike</div>
      <div class="facts">• Max. 20 participants<br>• Duration: 2 hours</div>
      <div class="meet">Meeting point: Under the big station clock at Rotterdam Central Station.</div>
    </div>
    <div class="tour__footer">
      <svg viewBox="0 0 16 16" aria-hidden="true"><circle cx="8" cy="8" r="6.5" fill="none" stroke="#fff" stroke-width="1.4"/><path d="M5.6 4.8l1.3-.3.7 1.7-.8.6c.4.9 1 1.5 1.9 1.9l.6-.8 1.7.7-.3 1.3C8.5 10 6 7.5 5.6 4.8Z" fill="#fff"/></svg>
      +31 (0)10 55 01 234
    </div>
  </div>
</section>

</body>
</html>
```